Corporate Two Sided Business Card

Looking for a Corporate "edgy" Modern look and feel for a business card

We are looking at two options. Dark background with our logo on it, white background with our logo on it - The background is more - Charcoal / Graphite then black

Details will be

Danielle Forsk

Licensee / Director

m. 0428 519 064

e. danielle@quorvela.com.au

quorvela.com.au

Target Market(s)

Professional Business people that refer use business and clients that own Investment Properties

Industry/Entity Type

Business

Contact Information for Business Card

Details will be

Danielle Forsk

Licensee / Director

m. 0428 519 064

quorvela.com.au

Font styles to use
Serif

Colors
000000
ec1f27
eeeeee
ffffff

Requirements
Must have
• Two options - White Background and Dark Background. - Two sided
Nice to have
• A design that is edgy, modern and new to look instead of boring style corporate cards - It should be a full integrated design
Should not have
• Block looking - Cheap.

```html
<!DOCTYPE html>
<html lang="en">
<head>
<meta charset="utf-8">
<title>Quorvela Business Card</title>
<link rel="stylesheet" href="https://fonts.googleapis.com/css2?family=Poppins:wght@500&family=Arimo:wght@400;700&display=swap">
<style>
  :root {
    --graphite: #3b3b3d;
    --graphite-dark: #2e2e30;
    --red: #ec1f27;
    --paper: #ffffff;
    --paper-shade: #eeeeee;
    --ink: #444446;
    --stage-top: #d9d9d9;
    --stage-bottom: #2a2a2a;
  }
  * { box-sizing: border-box; margin: 0; padding: 0; }
  html, body { width: 1200px; height: 997px; overflow: hidden; }
  body {
    background: linear-gradient(180deg, var(--stage-top) 0%, #8c8c8c 45%, var(--stage-bottom) 100%);
    font-family: "Arimo", Arial, sans-serif;
    position: relative;
  }
  .card {
    position: absolute;
    top: 341px;
    width: 540px;
    height: 315px;
    border-radius: 4px;
    box-shadow: 0 14px 30px rgba(0,0,0,.35);
    overflow: hidden;
  }
  .card--dark { left: 40px; background: linear-gradient(135deg, var(--graphite) 0%, var(--graphite-dark) 100%); }
  .card--light { left: 620px; background: linear-gradient(135deg, var(--paper) 0%, var(--paper-shade) 100%); }

  .brand {
    position: absolute;
    display: flex;
    align-items: center;
    gap: 10px;
    font-family: "Poppins", sans-serif;
    font-weight: 500;
    letter-spacing: .5px;
    line-height: 1;
  }
  .brand__mark { background: var(--red); flex: none; }
  .card--dark .brand { left: 50%; top: 50%; transform: translate(-50%, -50%); color: #f2f2f2; font-size: 58px; }
  .card--dark .brand__mark { width: 26px; height: 26px; }
  .card--light .brand { left: 62px; top: 78px; color: var(--ink); font-size: 50px; }
  .card--light .brand__mark { width: 22px; height: 22px; }

  .edge-tab {
    position: absolute;
    width: 14px;
    background: var(--graphite);
    border-radius: 7px;
  }
  .edge-tab--left { left: -7px; top: 140px; height: 160px; }
  .edge-tab--right { right: -7px; top: 20px; height: 140px; }

  .holder { position: absolute; left: 58px; top: 222px; }
  .holder__name { font-weight: 700; font-size: 15px; color: var(--ink); letter-spacing: .3px; text-transform: uppercase; }
  .holder__role { font-size: 13px; color: var(--red); margin-top: 3px; }

  .divider {
    position: absolute;
    left: 262px; top: 160px;
    width: 2px; height: 70px;
    background: linear-gradient(180deg, transparent, var(--red) 30%, var(--red) 70%, transparent);
  }

  .contacts { position: absolute; left: 282px; top: 166px; list-style: none; }
  .contacts li { display: flex; align-items: center; gap: 8px; font-size: 12px; color: var(--ink); height: 19px; }
  .contacts svg { width: 12px; height: 12px; flex: none; }
  .contacts .web { font-weight: 700; color: var(--red); font-size: 13px; letter-spacing: .8px; margin-top: 4px; }
</style>
</head>
<body>

  <section class="card card--dark" aria-label="Business card, dark side">
    <div class="brand"><span class="brand__mark"></span>quorvela</div>
  </section>

  <section class="card card--light" aria-label="Business card, light side">
    <span class="edge-tab edge-tab--left"></span>
    <span class="edge-tab edge-tab--right"></span>

    <div class="brand"><span class="brand__mark"></span>quorvela</div>

    <div class="holder">
      <p class="holder__name">Danielle Forsk</p>
      <p class="holder__role">Licensee / Director</p>
    </div>

    <span class="divider"></span>

    <ul class="contacts">
      <li>
        <svg viewBox="0 0 12 12" aria-hidden="true"><circle cx="6" cy="6" r="6" fill="#ec1f27"/><path d="M3.5 4.5c.5 1.8 2.2 3.5 4 4l.9-.9-1.2-.8-.6.5c-.7-.3-1.2-.8-1.5-1.5l.5-.6-.8-1.2z" fill="#fff"/></svg>
        0428 519 064
      </li>
      <li>
        <svg viewBox="0 0 12 12" aria-hidden="true"><circle cx="6" cy="6" r="6" fill="#ec1f27"/><rect x="3" y="4" width="6" height="4.2" fill="none" stroke="#fff" stroke-width=".8"/><path d="M3 4l3 2.3L9 4" fill="none" stroke="#fff" stroke-width=".8"/></svg>
        e.danielle@quorvela.com.au
      </li>
      <li class="web">WWW.QUORVELA.COM.AU</li>
    </ul>
  </section>

</body>
</html>
```